lawn sign

Lawn Sign
Roofing Gutters Windows

Target Market(s)

roofing

Font styles to use
Sans Serif

Colors
86cfc6
33a6d7
fbee3f
faa54b

Requirements
Must have
• my logo
Nice to have
• designer for now

```html
<!DOCTYPE html>
<html lang="en">
<head>
<meta charset="utf-8">
<title>Lawn Sign – Roofing Gutters Windows</title>
<link href="https://fonts.googleapis.com/css2?family=Archivo:wght@700;800;900&display=swap" rel="stylesheet">
<style>
  :root {
    --stage: #1b1b1b;
    --sign: #ffffff;
    --green: #5a9e33;
    --navy: #15243f;
    --label: #a9a9a9;
  }
  html, body {
    margin: 0;
    padding: 0;
    width: 1200px;
    height: 960px;
    overflow: hidden;
    background: var(--stage);
    font-family: "Archivo", Arial, sans-serif;
  }
  .canvas { position: relative; width: 1200px; height: 960px; }
  .sign {
    position: absolute;
    left: 200px; top: 220px;
    width: 800px; height: 520px;
    background: var(--sign);
    overflow: hidden;
  }
  .tagline-band {
    position: absolute;
    left: 254px; top: 0;
    width: 546px; height: 62px;
    background: var(--green);
    border-bottom-left-radius: 52px;
  }
  .tagline {
    position: absolute;
    left: 0; right: 0; top: 11px;
    text-align: center;
    color: #fff;
    font-weight: 800;
    font-size: 35px;
    line-height: 40px;
    letter-spacing: 0.2px;
  }
  .brand-mark {
    position: absolute;
    left: 44px; top: 46px;
    width: 118px; height: 118px;
    border-radius: 50%;
    background: var(--green);
  }
  .brand-name {
    position: absolute;
    right: 422px; top: 136px;
    text-align: right;
    color: var(--green);
    font-weight: 700;
    text-transform: uppercase;
  }
  .brand-name .primary { display: block; font-size: 30px; line-height: 34px; letter-spacing: 1px; }
  .brand-name .secondary { display: block; font-size: 19px; line-height: 25px; letter-spacing: 0.5px; }
  .divider {
    position: absolute;
    left: 404px; top: 88px;
    width: 8px; height: 173px;
    background: var(--green);
  }
  .services {
    position: absolute;
    left: 428px; top: 84px;
    margin: 0; padding: 0;
    list-style: none;
    color: var(--navy);
    font-weight: 900;
    font-size: 61px;
    line-height: 59px;
    letter-spacing: -0.5px;
  }
  .contact-band {
    position: absolute;
    left: 0; top: 288px;
    width: 800px; height: 164px;
    background: var(--green);
  }
  .call-tab {
    position: absolute;
    left: 50px; top: 0;
    width: 331px; height: 42px;
    background: var(--sign);
    border-bottom-left-radius: 40px;
    border-bottom-right-radius: 40px;
    color: var(--navy);
    font-weight: 900;
    font-size: 32px;
    line-height: 44px;
    text-align: center;
    letter-spacing: -0.3px;
  }
  .phone {
    position: absolute;
    left: 0; right: 0; top: 52px;
    text-align: center;
    color: #fff;
    font-weight: 900;
    font-size: 88px;
    line-height: 100px;
    letter-spacing: -1px;
  }
  .website {
    position: absolute;
    left: 0; right: 0; top: 466px;
    text-align: center;
    color: var(--navy);
    font-weight: 800;
    font-size: 32px;
    line-height: 40px;
  }
  .caption {
    position: absolute;
    left: 0; right: 0; top: 804px;
    text-align: center;
    color: var(--label);
    font-weight: 800;
    font-size: 24px;
    line-height: 28px;
  }
</style>
</head>
<body>
<div class="canvas">
  <section class="sign">
    <div class="tagline-band"><div class="tagline">We Restore &amp; Remodel</div></div>

    <div class="brand-mark"></div>
    <div class="brand-name">
      <span class="primary">Harlow</span>
      <span class="secondary">Restoration</span>
      <span class="secondary">Remodeling Group LLC</span>
    </div>

    <div class="divider"></div>
    <ul class="services">
      <li>ROOFING</li>
      <li>GUTTERS</li>
      <li>WINDOWS</li>
    </ul>

    <div class="contact-band">
      <div class="call-tab">CALL US TODAY</div>
      <div class="phone">(203) 555-0147</div>
    </div>

    <div class="website">www.harlowllc.com</div>
  </section>

  <div class="caption">YARD SIGN DESIGN</div>
</div>
</body>
</html>
```